Heading: Farrowdine (small font: under Farrowdine.. LIVE IN NOOSA)

We need a flyer for an upcoming Live show. (Double sided DL)
It is a magic & comedy show . We would like it to feel like its a high end classy show as it will be at a 5 star hotel. We like the look of all the Voltane Meridor posters (maybe google to have a look - I have attached some examples of what we like.
INFO FOR FLYER DOUBLE SIDED DL FLYER
Promo Photo- FOR FRONT OF FLYER : https://www.filecrate-example.net/s/qzt8wkp2rmex4la/Tobin%20Marsh%20Photography%20%28358%20of%20530%29.jpg?dl=0
A world-class experience combining comedy, magic and illusion.
Farrowdine has Performed live to over 1 million people.
*****
“HIGHLY ENTERTAINING (add 5 star graphics)
SENSATIONAL SHOW”
Loreth Abani
*****
"FARROWDINE’S SHOW WAS BETTER THAN GRESHAWN IN VEGAS. LOVED IT!”
Philippa & Conrad Tulliver
*****
“BEST MAGIC SHOW I’VE SEEN…
HAD US IN STITCHES LAUGHING THE WHOLE TIME”
Bunty Moe
SESSION ONE
FAMILY SHOW 5:30PM $38 PP
SESSION TWO
LATE SESSION 8PM $49.00 PP
NOOSA DATES
Thursday 24th Sept
Saturday 26th Sept
Thursday 1st October
Saturday 3rd October
BOOK ONLINE NOW - www.farrowdine-shows.com.au
TAMBERLY RESORT NOOSA LOGO (NEAR THE BOTTOM)
BACK OF FLYER
Add dinner to your award-winning show experience.
Dinner at Skelmoor by Reuben Farquell (ADD LOGO)
Two courses including a glass of wine $39.00
Two sittings, 6.30pm and 7pm.
Tables limited, so please book early to secure your table.
Booking details via Farrowdine-shows.com.au
Skelmoor Bar
Open from 12pm daily.
TAMBERLY Resort LOGO
Only a 5 minute stroll from Calloway Street, Noosa Heads
Vehicle Entry/Exit
Vehicle entry/exit as follows:
Ferntrell Drive (7pm-7am, Little Calloway Street),
Oakhurst Drive (7am-7pm, Brisk Way).
(please add map)
On-Site Parking
Limited parking is available on-site. Once parking is full, guests will be directed to park on Oakhurst Drive, with the resort buggy service available to transport guests up/down the driveway.
Covid Safety, Contact Tracing & distancing regulations are in place.
More Info: www.farrowdine-shows.com.au

```html
<!DOCTYPE html>
<html lang="en">
<head>
<meta charset="utf-8">
<title>Farrowdine – Live in Noosa</title>
<link rel="stylesheet" href="https://fonts.googleapis.com/css2?family=Anton&family=Montserrat:wght@400;600;700;800&display=swap">
<style>
  :root {
    --backdrop: #e6e6e8;
    --purple-deep: #2a0c52;
    --purple: #3d1577;
    --purple-light: #5a2aa0;
    --glow: #b07ae8;
    --gold: #e8b54a;
    --gold-light: #f7dc8c;
    --gold-dark: #b8862a;
    --white: #ffffff;
    --muted: #d9cdef;
  }
  * { box-sizing: border-box; margin: 0; padding: 0; }
  html, body { width: 800px; height: 1200px; overflow: hidden; }
  body {
    background: var(--backdrop);
    display: flex; align-items: center; justify-content: center;
    font-family: "Montserrat", Arial, sans-serif;
    color: var(--white);
  }
  .flyer {
    width: 540px; height: 1140px;
    background: radial-gradient(ellipse at 50% 30%, var(--purple-light) 0%, var(--purple) 45%, var(--purple-deep) 100%);
    box-shadow: 0 6px 24px rgba(0,0,0,.25);
    padding: 34px 36px 30px;
    display: flex; flex-direction: column; align-items: center;
  }
  .title {
    font-family: "Anton", Impact, sans-serif;
    font-size: 88px; line-height: 1; letter-spacing: 1px;
    background: linear-gradient(180deg, var(--gold-light) 0%, var(--gold) 55%, var(--gold-dark) 100%);
    -webkit-background-clip: text; background-clip: text; color: transparent;
  }
  .subtitle {
    margin-top: 12px;
    border: 2px solid var(--gold);
    background: rgba(255,255,255,.08);
    padding: 7px 30px;
    font-weight: 700; font-size: 20px; letter-spacing: 4px;
  }
  .hero-art {
    width: 380px; height: 320px; margin-top: 22px;
    background: radial-gradient(ellipse at 50% 50%, var(--glow) 0%, rgba(138,79,216,.55) 35%, rgba(61,21,119,0) 70%);
  }
  .reviews {
    margin-top: 18px; width: 100%;
    display: grid; grid-template-columns: 1fr 1fr; gap: 18px 26px;
  }
  .review { text-align: center; }
  .review--wide { grid-column: 1 / 3; padding: 0 60px; }
  .quote-mark {
    font-family: "Anton", Impact, sans-serif;
    color: var(--gold); font-size: 40px; line-height: .8; display: block;
  }
  .review-text {
    font-weight: 700; font-size: 13px; line-height: 1.35; text-transform: uppercase; margin-top: 4px;
  }
  .review-name { color: var(--gold); font-size: 11px; font-weight: 600; margin-top: 4px; }
  .rule { width: 100%; height: 1px; background: linear-gradient(90deg, transparent, var(--gold), transparent); margin: 24px 0 18px; flex-shrink: 0; }
  .sessions, .dates { width: 100%; display: grid; grid-template-columns: 1fr 1fr; gap: 26px; text-align: center; }
  .label { color: var(--gold); font-size: 11px; font-weight: 700; letter-spacing: 2px; text-transform: uppercase; }
  .session-name { font-weight: 800; font-size: 18px; margin-top: 3px; }
  .session-price { color: var(--gold-light); font-weight: 700; font-size: 16px; margin-top: 2px; }
  .dates { margin-top: 20px; }
  .date-list { font-size: 13px; font-weight: 600; line-height: 1.6; margin-top: 3px; }
  .footer {
    margin-top: auto; width: 100%;
    display: grid; grid-template-columns: 110px 1fr; gap: 16px; align-items: end;
  }
  .portrait {
    width: 110px; height: 136px;
    background: linear-gradient(180deg, #4b3a5e 0%, #1c1226 100%);
    border: 2px solid var(--gold);
  }
  .info { font-size: 11px; line-height: 1.45; color: var(--muted); }
  .info strong { color: var(--white); }
  .actions { display: flex; align-items: center; justify-content: space-between; margin-top: 12px; gap: 10px; }
  .book-btn {
    background: linear-gradient(180deg, var(--gold-light), var(--gold));
    color: var(--purple-deep); font-weight: 800; font-size: 9.5px;
    padding: 7px 10px; white-space: nowrap;
  }
  .venue { display: flex; align-items: center; gap: 6px; font-size: 10px; font-weight: 700; color: var(--white); letter-spacing: 1px; }
  .venue-mark { width: 10px; height: 10px; background: var(--white); flex-shrink: 0; }
</style>
</head>
<body>
  <main class="flyer">
    <h1 class="title">FARROWDINE</h1>
    <p class="subtitle">LIVE IN NOOSA</p>

    <div class="hero-art" role="img" aria-label="Illustration of a magician's top hat with a burst of light rising from it"></div>

    <section class="reviews">
      <article class="review">
        <span class="quote-mark">“</span>
        <p class="review-text">Highly entertaining. Sensational show</p>
        <p class="review-name">Loreth Abani</p>
      </article>
      <article class="review">
        <span class="quote-mark">“</span>
        <p class="review-text">Farrowdine's show was better than Greshawn in Vegas. Loved it!</p>
        <p class="review-name">Philippa &amp; Conrad Tulliver</p>
      </article>
      <article class="review review--wide">
        <span class="quote-mark">“</span>
        <p class="review-text">Best magic show I've seen… had us in stitches laughing the whole time</p>
        <p class="review-name">Bunty Moe</p>
      </article>
    </section>

    <div class="rule"></div>

    <section class="sessions">
      <div class="session">
        <p class="label">Session One</p>
        <p class="session-name">Family Show</p>
        <p class="session-price">5:30pm $38 PP</p>
      </div>
      <div class="session">
        <p class="label">Session Two</p>
        <p class="session-name">Late Session</p>
        <p class="session-price">8pm $49.00 PP</p>
      </div>
    </section>

    <section class="dates">
      <div>
        <p class="label">Noosa Dates</p>
        <p class="date-list">Thursday 24th Sept<br>Saturday 26th Sept</p>
      </div>
      <div>
        <p class="label">Noosa Dates</p>
        <p class="date-list">Thursday 1st October<br>Saturday 3rd October</p>
      </div>
    </section>

    <div class="rule"></div>

    <footer class="footer">
      <div class="portrait" role="img" aria-label="Promo photo of the performer Farrowdine"></div>
      <div>
        <p class="info"><strong>A world-class experience combining comedy, magic and illusion.</strong><br>Farrowdine has performed live to over 1 million people.</p>
        <div class="actions">
          <span class="book-btn">BOOK ONLINE NOW – www.farrowdine-shows.com.au</span>
        </div>
        <div class="actions">
          <span class="venue"><span class="venue-mark"></span>TAMBERLY RESORT NOOSA</span>
        </div>
      </div>
    </footer>
  </main>
</body>
</html>
```